HTP Brochure redesign

We need a brochure redesign for a new company based in UK. Harbourline Talent Partners (HTP) is a new generation of headhunters within the Payment & Card industries across the EMEA & Asia Pac including the Emerging Markets. Our current design was designed by myself, I am looking for a more professional touch.

Target Market(s)

ePayment & Card industries

Industry/Entity Type

It Company

Font styles to use
Serif

Requirements
Must have
• Must be engaging, clear and clean. The industries are very fast paced, high tech business such as Kivano, Tallamex, Brisqual
Nice to have
• Colour, cool trendy high tech design, Please keep logo. Feel free to cut text to improve design
Should not have
• Design should be simple child like, it must be better than what i already have...

```html
<!DOCTYPE html>
<html lang="en">
<head>
<meta charset="utf-8">
<title>HTP Brochure</title>
<link rel="stylesheet" href="https://fonts.googleapis.com/css2?family=Lato:wght@300;400;700&family=Crimson+Text:wght@400;600&family=Dancing+Script:wght@500&display=swap">
<style>
:root{
  --stage:#303538;
  --paper:#ffffff;
  --ink:#2f3336;
  --ink-soft:#55595c;
  --red:#d6222a;
  --orange:#f08a1c;
  --green:#4cae19;
  --blue:#54bce8;
  --navy:#1c2a6b;
  --slate:#4d5357;
  --pink:#e98a99;
  --mint:#8ccf7e;
}
*{margin:0;padding:0;box-sizing:border-box}
html,body{width:1200px;height:1000px;overflow:hidden}
body{background:var(--stage);position:relative;font-family:"Crimson Text",Georgia,serif;color:var(--ink)}
.page{position:absolute;background:var(--paper);overflow:hidden}
.stripe{position:absolute;left:0;top:0;width:100%;height:5px}
.stripe--multi{background:linear-gradient(90deg,var(--navy) 0 8%,var(--orange) 8% 18%,var(--green) 18% 32%,var(--red) 32% 44%,var(--orange) 44% 52%,var(--green) 52% 62%,var(--blue) 62% 72%,var(--orange) 72% 80%,var(--green) 80% 90%,var(--navy) 90% 100%)}
.stripe--warm{background:linear-gradient(90deg,var(--red),var(--orange) 70%,var(--orange))}
.stripe--cool{background:linear-gradient(90deg,var(--blue),var(--blue) 55%,var(--navy))}
.sans{font-family:"Lato",Arial,sans-serif}
.body-copy{font-size:4.6px;line-height:6px;color:var(--ink)}
.body-copy p{margin-bottom:4px}

/* cover */
.cover{left:412px;top:40px;width:370px;height:286px}
.cover__name{position:absolute;left:0;width:100%;top:104px;text-align:center;font-family:"Lato",Arial,sans-serif;font-weight:400;font-size:24px;letter-spacing:1px;color:var(--ink-soft)}
.cover__mark{position:absolute;left:172px;top:68px;width:26px;height:26px;border-radius:50%;background:var(--green)}
.cover__tagline{position:absolute;left:0;width:100%;top:137px;text-align:center;font-family:"Dancing Script",cursive;font-size:14px;color:var(--green)}
.cover__title{position:absolute;left:0;width:100%;top:163px;text-align:center;font-family:"Lato",Arial,sans-serif;font-size:10px;color:var(--ink)}
.cover__rule{position:absolute;left:76px;width:218px;top:205px;border-top:1px solid #8a8d90}
.cover__web{position:absolute;left:0;width:100%;top:237px;text-align:center;font-family:"Lato",Arial,sans-serif;font-size:8.5px;color:var(--ink)}

/* intro */
.intro{left:193px;top:346px;width:390px;height:274px}
.intro__deco{position:absolute;left:0;top:0}
.intro__title{position:absolute;left:17px;top:52px;font-family:"Lato",Arial,sans-serif;font-weight:400;font-size:21px;line-height:27px;color:var(--ink)}
.intro__title .accent{color:var(--red)}
.intro__copy{position:absolute;left:17px;top:113px;width:296px}

/* expertise */
.expertise{left:597px;top:346px;width:390px;height:274px}
.services{position:absolute;left:0;top:6px;width:150px;height:150px;border-radius:50%;background:var(--blue);color:#fff;text-align:center}
.services__head{font-family:"Lato",Arial,sans-serif;font-size:13px;line-height:14px;margin-top:47px}
.services__lead{font-size:5px;margin-top:4px}
.services__list{list-style:none;font-size:5px;line-height:6.4px;margin-top:5px}
.photo-round{position:absolute;left:10px;top:175px;width:90px;height:90px;border-radius:50%;background:radial-gradient(circle at 45% 40%,#dfe7ee,#9fb3c4 60%,#5b6f82)}
.expertise__title{position:absolute;left:161px;top:24px;font-family:"Lato",Arial,sans-serif;font-weight:300;font-size:21px;line-height:27px;color:var(--blue)}
.expertise__copy{position:absolute;left:161px;top:80px;width:225px}
.different{position:absolute;left:161px;top:199px;width:229px;height:60px;background:var(--slate);color:#fff;text-align:center}
.different__head{font-family:"Lato",Arial,sans-serif;font-size:11.5px;margin-top:10px}
.different__copy{font-size:4.6px;line-height:5.8px;padding:4px 20px 0}

/* offer */
.offer{left:193px;top:637px;width:390px;height:275px}
.offer__lines{position:absolute;left:0;width:100%;top:25px;text-align:center;font-size:7.5px;line-height:9px;color:var(--ink)}
.offer__title{position:absolute;left:0;width:100%;top:78px;text-align:center;font-family:"Lato",Arial,sans-serif;font-weight:300;font-size:21px;line-height:27px;color:var(--ink)}
.offer__title .accent{color:var(--green)}
.offer__copy{position:absolute;left:34px;top:136px;width:322px;text-align:center;font-size:4.6px;line-height:5.8px}
.reasons{position:absolute;left:0;top:163px;width:100%;height:112px;background:var(--green)}
.reasons__box{position:absolute;left:14px;top:10px;width:154px;height:90px;border:1px solid #fff;color:#fff;font-family:"Lato",Arial,sans-serif;font-weight:300;font-size:18px;line-height:26px;padding:7px 0 0 13px}
.reasons__list{position:absolute;left:185px;top:9px;width:196px;list-style:none;color:#fff}
.reasons__list li{position:relative;padding-left:16px;font-size:4.6px;line-height:5.6px;margin-bottom:6.5px}
.reasons__list li span{position:absolute;left:0;top:-2px;font-family:"Lato",Arial,sans-serif;font-size:9px;line-height:9px}

/* contact */
.contact{left:597px;top:637px;width:390px;height:275px}
.contact__title{position:absolute;left:14px;top:28px;font-family:"Lato",Arial,sans-serif;font-weight:300;font-size:21px;letter-spacing:1px;word-spacing:8px;color:var(--ink-soft)}
.contact__sub{position:absolute;left:14px;top:60px;font-family:"Lato",Arial,sans-serif;font-size:12px;color:var(--green)}
.contact__copy{position:absolute;left:14px;top:81px;width:168px}
.photo-keys{position:absolute;left:190px;top:32px;width:181px;height:89px;border-radius:10px;background:linear-gradient(120deg,#f4f5f6,#c9cdd1 55%,#8d949b)}
.channels{position:absolute;left:14px;top:155px;width:360px;height:14px}
.channel{position:absolute;top:0;display:flex;align-items:center;gap:8px;font-family:"Lato",Arial,sans-serif;font-size:5.5px;font-weight:700;color:var(--ink)}
.join{position:absolute;left:0;width:100%;top:212px;text-align:center;font-family:"Lato",Arial,sans-serif;font-weight:300;font-size:19px;color:var(--ink-soft)}
.networks{position:absolute;left:0;width:100%;top:248px;display:flex;justify-content:center;gap:10px;font-family:"Lato",Arial,sans-serif;font-size:7px;font-weight:700;color:var(--slate)}
</style>
</head>
<body>

<section class="page cover">
  <div class="stripe stripe--multi"></div>
  <div class="cover__mark"></div>
  <div class="cover__name">HTP</div>
  <div class="cover__tagline">Helping you Succeed</div>
  <div class="cover__title">New Generation of Global Headhunters</div>
  <div class="cover__rule"></div>
  <div class="cover__web">www.harbourlinetp.com</div>
</section>

<section class="page intro">
  <div class="stripe stripe--warm"></div>
  <svg class="intro__deco" width="390" height="274" viewBox="0 0 390 274">
    <circle cx="350" cy="135" r="165" fill="none" stroke="var(--pink)" stroke-width="1"/>
    <circle cx="278" cy="296" r="92" fill="none" stroke="var(--mint)" stroke-width="1"/>
  </svg>
  <h1 class="intro__title"><span class="accent">HTP</span> – NEW GENERATION<br>OF HEADHUNTERS</h1>
  <div class="intro__copy body-copy">
    <p>Harbourline Talent Partners (HTP) is a new generation of headhunters that combines an understanding of global recruitment within the Card &amp; Payment industry. We are focused on innovative, creative and effective talent acquisition and we like to think we are getting rather good at it. Our expertise lies within Card &amp; Payment businesses across the UK, EMEA and Asia Pac, and we never take a one-size-fits-all approach.</p>
    <p>Our aim is simple – to become the most respected Card &amp; Payment headhunter in the market. We consult, we advise and we will execute your plan. If you are a candidate, once again we have one very clear goal: to find the role that fits you. The result is a successful career and a successful business that meets the objectives of both employee and employer.</p>
    <p>Start working together with HTP to find better hires for your organisation, faster and more cost effectively. Don't let another day go by using outdated recruiting methods.</p>
  </div>
</section>

<section class="page expertise">
  <div class="stripe stripe--cool"></div>
  <div class="services">
    <div class="services__head">OUR<br>SERVICES</div>
    <div class="services__lead">HTP acts as an extension of your<br>company when recruiting</div>
    <div>–</div>
    <ol class="services__list">
      <li>1. Permanent Placement Global Staffing Solutions</li>
      <li>2. Temporary/Contract Global Staffing Solutions</li>
      <li>3. Global Outplacement &amp; Career Transition</li>
      <li>4. CV Review Service</li>
    </ol>
  </div>
  <div class="photo-round" role="img" aria-label="Photo of consultants in a business meeting"></div>
  <h2 class="expertise__title">OUR INTERNATIONAL<br>EXPERTISE</h2>
  <div class="expertise__copy body-copy">
    <p>HTP is a global company making talent management work locally. The ability to understand the diverse markets of Europe, Africa, Middle East and Asia including the Emerging Markets offers a real advantage to companies with international hiring needs. HTP has established partnerships across the world and has achieved notable success internationally. We help customers around the world implement successful talent management initiatives that identify the right people, in the right places, at the right time. If you want to compete in today's market you need a global presence and recruitment experts with global capabilities.</p>
    <p>We also provide a comprehensive range of human resources management services to the global markets, with access to an instant network of highly qualified professionals. Our international assignments are underpinned by consistent professional delivery and clear, regular reporting. Let HTP show you how we will identify and attract the highest achievers to your business.</p>
  </div>
  <div class="different">
    <div class="different__head">WHAT MAKES US DIFFERENT?</div>
    <div class="different__copy">We know the importance of acquiring passive talent. To this end we can quickly headhunt and deliver candidates using a combination of social media recruiting, online networking tools and traditional headhunting methodologies. Here's how we do it differently.</div>
  </div>
</section>

<section class="page offer">
  <div class="stripe stripe--multi"></div>
  <div class="offer__lines">
    We don't want retainers<br>
    We don't want £10,000 upfront just to provide research<br>
    We don't string out the search process which is often in the interests of the<br>
    search firm not the client
  </div>
  <h2 class="offer__title"><span class="accent">WHAT</span> CAN A HTP<br>HEADHUNTER DO FOR YOU</h2>
  <p class="offer__copy">No one is more aware and engaged in social media than an HTP headhunter – the advantages to us are obvious. Rather than recognising social media as a recruitment solution, employers are instead realising that they need to work more closely with us in order to get their hiring right first time – not making the mistake of investing time and resources into social media without a return on their investment (ROI).</p>
  <div class="reasons">
    <div class="reasons__box">GREAT<br>REASONS<br>TO USE HTP</div>
    <ol class="reasons__list">
      <li><span>1.</span>Time Saving: We don't have to have numerous meetings, we don't call you 20 times a day ... we just get on with the work efficiently... and deliver excellent candidates.</li>
      <li><span>2.</span>Global Recruiting Experts: Experts in recruiting "best passive talent", with a high percentage of our talent pool sourced through state of the art search methodologies.</li>
      <li><span>3.</span>Our Guarantee: We're so confident of our candidates' quality that we offer a 100 days, 100% free hire replacement.</li>
      <li><span>4.</span>Industry Expertise: Card &amp; Payment industry is constantly evolving on an almost daily basis. It's difficult to keep up with the changes – they happen so fast; however here at HTP we do!</li>
      <li><span>5.</span>Cost Saving: Global Executive Search service however only charging a contingency fee. In other words no placement, no fee.</li>
    </ol>
  </div>
</section>

<section class="page contact">
  <div class="stripe stripe--multi"></div>
  <h2 class="contact__title">CONTACT US!</h2>
  <div class="contact__sub">ANYTIME, ANYWHERE!</div>
  <p class="contact__copy body-copy">HTP believe that 'core hours' can't really exist when dealing with the modern business of career consultation. As such, we can be contacted any time, and we are happy to meet you out of your 'core hours' – assisting you how it suits you. Evenings and weekends may suit your schedule best. Not a problem at all. We prefer that we meet when you aren't worried about deadlines. Call or email us – again whatever suits you best. You have our guarantee that any enquiry is treated with the strictest confidence.</p>
  <div class="photo-keys" role="img" aria-label="Photo of a finger pressing a desk phone keypad"></div>
  <div class="channels">
    <div class="channel" style="left:0">
      <svg width="11" height="10" viewBox="0 0 11 10"><path d="M1 4 Q5.5 0 10 4 L8.5 5.5 L7 4.2 L4 4.2 L2.5 5.5 Z" fill="var(--ink)"/><rect x="3.5" y="5" width="4" height="4" rx="1" fill="var(--ink)"/></svg>
      +44(0)333 010 456 2
    </div>
    <div class="channel" style="left:138px">
      <svg width="11" height="9" viewBox="0 0 11 9"><rect x="0.5" y="0.5" width="10" height="8" fill="var(--ink)"/><path d="M0.5 0.5 L5.5 5 L10.5 0.5" fill="none" stroke="#fff" stroke-width="1"/></svg>
      enquiries@harbourlinetp.com
    </div>
    <div class="channel" style="left:274px">
      <svg width="11" height="11" viewBox="0 0 11 11"><circle cx="5.5" cy="5.5" r="5" fill="var(--ink)"/><ellipse cx="5.5" cy="5.5" rx="2" ry="5" fill="none" stroke="#fff" stroke-width="0.7"/><line x1="0.5" y1="5.5" x2="10.5" y2="5.5" stroke="#fff" stroke-width="0.7"/></svg>
      www.harbourlinetp.com
    </div>
  </div>
  <div class="join">JOIN US !</div>
  <div class="networks">
    <span>Netlinks</span><span>Frendo</span><span>Chirpa</span><span>Xeno</span><span>Plexa</span>
  </div>
</section>

</body>
</html>
```